Oil and Gas Company: Letterhead Design

In short we need a professional company letterhead designed for our Oil and Gas company.

We would like to keep the design simple and professional. Letterhead to include the company logo and color scheme, front page and continuation pages.

For reference, see attached logo below with our company logo and color scheme.

Target Market(s)

Oil & Gas Market

Industry/Entity Type

Oil And Gas

Font styles to use
Sans Serif

Requirements
Must have
• Letterhead must contain a front page & continuation page.
• Must be simple and professional in design.
• Follow our logo and color scheme.
Nice to have
• I would like to have the logo embedded in the bottom right hand portion of the page to provide some depth into the letterhead.

```html
<!DOCTYPE html>
<html lang="en">
<head>
<meta charset="utf-8">
<title>Harlow Ridge Energy – Letterhead</title>
<link href="https://fonts.googleapis.com/css2?family=Jost:wght@400;500&display=swap" rel="stylesheet">
<style>
  :root {
    --brand-red: #e3212b;
    --brand-blue: #0f54a3;
    --paper: #ffffff;
    --backdrop: #eceef1;
    --body-text: #7a7a7a;
    --ink: #1c1c1c;
    --mark-navy: #1d3f73;
  }
  * { margin: 0; padding: 0; box-sizing: border-box; }
  html, body { width: 1200px; height: 1189px; overflow: hidden; }
  body {
    background: var(--backdrop);
    font-family: "Jost", "Futura", sans-serif;
    position: relative;
  }
  .sheet {
    position: absolute;
    background: var(--paper);
    overflow: hidden;
  }
  .sheet--front { left: 53px; top: 55px; width: 510px; height: 658px; }
  .sheet--continuation { left: 608px; top: 407px; width: 555px; height: 717px; }

  .cover-artwork {
    position: absolute;
    left: 0; top: 150px; right: 0; bottom: 0;
    background: linear-gradient(135deg, var(--brand-red) 0%, var(--brand-red) 45%, var(--brand-blue) 100%);
  }

  .header-band {
    position: absolute;
    left: 0; top: 0; right: 0; height: 120px;
    background: var(--brand-blue);
    border-bottom: 6px solid var(--brand-red);
  }
  .footer-band {
    position: absolute;
    left: 0; right: 0; bottom: 0; height: 34px;
    background: var(--brand-blue);
    border-top: 6px solid var(--brand-red);
  }

  .company-name {
    position: absolute;
    font-weight: 500;
    font-size: 8.5px;
    letter-spacing: 0.04em;
    line-height: 1.2;
    text-transform: uppercase;
    text-align: center;
  }
  .company-name .name-square {
    display: block;
    width: 12px; height: 12px;
    margin: 0 auto 8px;
  }
  .sheet--front .company-name { left: 21px; top: 60px; color: var(--mark-navy); }
  .sheet--front .name-square { background: var(--mark-navy); }
  .sheet--continuation .company-name { right: 22px; top: 40px; color: var(--paper); }
  .sheet--continuation .name-square { background: var(--paper); }

  .letter-body {
    position: absolute;
    left: 65px; top: 172px; width: 422px;
    color: var(--body-text);
    font-size: 13px;
    line-height: 16px;
  }
  .letter-body p + p { margin-top: 15px; }

  .signature-label {
    position: absolute;
    right: 68px; top: 563px;
    color: var(--ink);
    font-size: 13px;
  }
  .signature-line {
    position: absolute;
    left: 400px; top: 604px;
    width: 87px; height: 1.5px;
    background: var(--ink);
  }
</style>
</head>
<body>

  <section class="sheet sheet--front" aria-label="Front page">
    <div class="cover-artwork" role="img" aria-label="Red and blue geometric cover artwork"></div>
    <div class="company-name"><span class="name-square"></span>Harlow Ridge<br>Energy</div>
  </section>

  <section class="sheet sheet--continuation" aria-label="Continuation page">
    <div class="header-band"></div>
    <div class="company-name"><span class="name-square"></span>Harlow Ridge<br>Energy</div>

    <div class="letter-body">
      <p>Solum nullam principes vis no, eleifend postulant mediocrem ut est, ad tota partem quo. Vix lorem putant scribentur no, mea meis solet melius no, pri feugait noluisse appetere no. Ei mea graece suscipit, fastidii probatus est et. Duo ut oportere iudicabit, exerci laoreet vim id. An vidit quidam cum, ceteros phaedrum sit ea. Mollis incorrupte in vix. Noster mnesarchum vix ei.</p>
      <p>Ius te maluisset voluptatum quaerendum, no discere saperet persequeris cum, no pro nonumy partem phaedrum. Mel mazim corpora te. Has ad aeque mucius impetus, vel latian regione appetere ne. Porro voluptatum ius ut, ei docendi eloquentiam sea. Ne mandamus dignissim efficiendi eum, est id tota insolens, eu per facete latine.</p>
      <p>Sea te explicari conceptam definitionem, soluta constituto duo ad, usu an laudem latine voluptaria. Eam magna repudiare forensibus an. In nam euismod explicari voluptatibus. Petentium dissentiet ex eum, in eam ludus tantas aperiam. Eu est latine feugait suavitate.</p>
      <p>Eum ei augue voluptua copiosae. Vis cu altera noluisse intellegat. At vis probatus perpetua. Tale alterum interesset ne quo, est ad exerci oblique recusabo, eu sit simul legendos antiopam. Qui tacimates tractatos ad, delectus sapientem omittantur ut vis. Pro te graece equidem ancillae, indoctum molestiae eam ea.</p>
    </div>

    <div class="signature-label">Signature</div>
    <div class="signature-line"></div>

    <div class="footer-band"></div>
  </section>

</body>
</html>
```